The Corvane Agency

We are a pr, social media and strategy agency specializing in the pet industry. We would like a new dynamic design of our existing website. We think it is currently outdated and looks too corporate. We would like it to look more consumer oriented as we primarily market pet products. We would like warm imagery involving pets and while pets are fun, this is still a business website and needs to maintain a professional look. We are hired by business owners and executives.
I would like some of our work featured on the home page.
Our primary service tabs are:
Public Relations
Social Media
Product Consulting
Most of the content will remain the same but we are open to suggestions!
Our current website can be found at www.lorvishdogpr.com.
We are open to other colors than in our logo and on our current page.
This is a design only project and will not require programming. The selected designer will need to provide at least one interior page in addition to the home page.

Industry/Entity Type

Pet

Requirements
Should not have
• Cartoon type figures. Pet puns.

```html
<!DOCTYPE html>
<html lang="en">
<head>
<meta charset="utf-8">
<title>The Corvane Agency</title>
<link rel="stylesheet" href="https://fonts.googleapis.com/css2?family=Oswald:wght@300;400;700&family=Alfa+Slab+One&family=Open+Sans:wght@400;600&display=swap">
<style>
:root{
  --orange:#f0560a;
  --orange-bright:#ff5a00;
  --rust:#b05613;
  --rust-dark:#8e430d;
  --sand:#c9c1b3;
  --ink:#222;
  --line:#e4e4e4;
  --gold:#ffc93a;
  --mocha:#8a7860;
}
*{margin:0;padding:0;box-sizing:border-box}
html,body{width:784px;height:1200px;overflow:hidden;background:#fff}
body{position:relative;font-family:Arial,Helvetica,sans-serif;color:var(--ink)}
.abs{position:absolute}
.topbar{left:0;top:0;width:784px;height:35px;background:var(--orange)}
.topbar-word{top:3px;font-family:'Oswald',sans-serif;font-weight:300;font-size:21px;color:#fff}
.brand-tab{left:0;top:0}
.brand-name{left:284px;top:8px;width:204px;text-align:center;font-family:'Oswald',sans-serif;font-weight:400;font-size:19px;color:#e2231a}
.hero-photo{left:0;top:35px;width:600px;height:309px;background:radial-gradient(ellipse at 45% 60%,#d99452 0%,#e9c59b 35%,#fff 72%)}
.hero-title{left:367px;top:91px;font-family:'Oswald',sans-serif;font-weight:300;font-size:31px;line-height:32px;color:#7a7a7a;letter-spacing:-1px;white-space:nowrap}
.hero-text{left:369px;top:129px;width:320px;font-size:9.6px;line-height:12px;color:#888}
.slide-arrow{top:167px;width:24px;height:24px;border-radius:50%;background:var(--gold)}
.band{left:0;top:344px;width:784px;height:154px;background:var(--rust)}
.nav{left:0;top:332px}
.nav-item{top:348px;font-family:'Oswald',sans-serif;font-weight:300;font-size:18px;color:#fff;letter-spacing:-.4px}
.social-circle{top:412px;width:48px;height:48px;border-radius:50%;background:#fff;display:flex;align-items:center;justify-content:center}
.social-circle svg{width:26px;height:26px;fill:var(--rust)}
.social-label{top:466px;width:110px;text-align:center;font-family:'Oswald',sans-serif;font-weight:300;font-size:11.5px;color:#fff;letter-spacing:-.3px}
.kitten-photo{left:12px;top:540px;width:308px;height:228px;background:radial-gradient(ellipse at 40% 55%,#b9ac98 0%,#ddd6cb 40%,#fff 72%)}
.welcome-title{left:270px;top:546px;font-family:'Alfa Slab One',serif;font-size:26px;color:var(--mocha);letter-spacing:1px}
.welcome-text{left:239px;top:588px;width:222px;font-size:9.6px;line-height:11.6px;color:#222}
.welcome-text p+p{margin-top:11px}
.news-heading{left:509px;top:532px;font-family:'Oswald',sans-serif;font-weight:300;font-size:26px;color:#555;letter-spacing:-1px}
.news-date{left:506px;width:40px;height:40px;border-radius:50%;background:var(--orange-bright);color:#fff;text-align:center;font-family:'Oswald',sans-serif;font-weight:700}
.news-date b{display:block;font-size:17px;line-height:17px;margin-top:5px}
.news-date span{display:block;font-size:9px;line-height:10px}
.news-title{left:554px;width:190px;font-family:'Oswald',sans-serif;font-weight:700;font-size:15px;line-height:18px;color:var(--orange-bright);letter-spacing:-.8px}
.news-text{left:506px;width:220px;font-size:9.2px;line-height:14.4px;color:#777}
.news-text a{color:#444;font-weight:bold;text-decoration:underline}
.rule{left:26px;width:728px;height:1px;background:var(--line)}
.client-frame{top:857px;width:120px;height:91px;background:#e6e6e6;padding:8px}
.client-photo{width:104px;height:75px}
.client-name{top:956px;font-family:'Open Sans',sans-serif;font-size:12.5px;color:#222}
.client-text{top:994px;width:164px;font-size:9.6px;line-height:11.6px;color:#888}
.more-link{right:30px;top:1090px;font-family:'Open Sans',sans-serif;font-weight:600;font-size:14px;color:#555;display:flex;align-items:center;gap:6px}
.more-link i{width:9px;height:9px;border-radius:50%;background:#999;display:inline-block}
.footer{left:0;top:1146px;width:784px;height:54px;background:var(--orange);display:flex;align-items:center;justify-content:center;gap:6px;color:#fff;font-size:8.5px}
.footer strong{font-family:'Oswald',sans-serif;font-weight:700;font-size:12px;letter-spacing:-.3px}
</style>
</head>
<body>

<div class="abs topbar"></div>
<svg class="abs brand-tab" width="784" height="60" viewBox="0 0 784 60">
  <polygon points="260,35 284,35 272,56" fill="#bbb"/>
  <polygon points="488,35 512,35 500,59" fill="#bbb"/>
  <polygon points="300,0 474,0 492,35 282,35" fill="#fff"/>
</svg>
<div class="abs topbar-word" style="left:194px">Welcome to</div>
<div class="abs topbar-word" style="left:498px">website.</div>
<div class="abs brand-name">The Corvane Agency</div>

<div class="abs hero-photo" role="img" aria-label="Photo of a ginger kitten playing on a resting bulldog"></div>
<h1 class="abs hero-title">REDEFINING PET ASSOCIATIONS</h1>
<p class="abs hero-text">The power of any association is the strenght of unity. We have managed a wide range of pet-related associations and tradeshows, brining teams together to deliver outstanding results.</p>
<div class="abs slide-arrow" style="left:13px"></div>
<div class="abs slide-arrow" style="left:744px"></div>

<div class="abs band"></div>
<svg class="abs nav" width="784" height="58" viewBox="0 0 784 58">
  <polygon points="70,12 84,0 110,46" fill="var(--rust-dark)"/>
  <polygon points="716,0 690,46 704,12" fill="var(--rust-dark)"/>
  <polygon points="84,0 706,0 676,56 116,56" fill="var(--sand)"/>
</svg>
<nav>
  <div class="abs nav-item" style="left:150px">HOME</div>
  <div class="abs nav-item" style="left:229px">PUBLIC RELATIONS</div>
  <div class="abs nav-item" style="left:386px">SOCIAL MEDIA</div>
  <div class="abs nav-item" style="left:516px">PRODUCT CONSULTING</div>
</nav>

<div class="abs social-circle" style="left:122px"><svg viewBox="0 0 24 24"><path d="M12 21l-1.5-1.3C5 15 2 12.2 2 8.6 2 5.8 4.2 3.6 7 3.6c1.9 0 3.7.9 5 2.4 1.3-1.5 3.1-2.4 5-2.4 2.8 0 5 2.2 5 5 0 3.6-3 6.4-8.5 11.1z"/></svg></div>
<div class="abs social-circle" style="left:222px"><svg viewBox="0 0 24 24"><path d="M10 3h4v7h7v4h-7v7h-4v-7H3v-4h7z"/></svg></div>
<div class="abs social-circle" style="left:318px"><svg viewBox="0 0 24 24"><circle cx="12" cy="4.5" r="2.5"/><rect x="9.5" y="9" width="5" height="13"/></svg></div>
<div class="abs social-circle" style="left:414px"><svg viewBox="0 0 24 24"><circle cx="6" cy="12" r="3.5"/><circle cx="18" cy="5.5" r="3.5"/><circle cx="18" cy="18.5" r="3.5"/><path d="M6 12L18 5.5M6 12l12 6.5" stroke="#b05613" stroke-width="2.2" fill="none"/></svg></div>
<div class="abs social-circle" style="left:510px"><svg viewBox="0 0 24 24"><rect x="4" y="3" width="16" height="18" rx="1.5"/><path d="M7.5 8h9M7.5 12h9M7.5 16h6" stroke="#fff" stroke-width="1.8"/></svg></div>
<div class="abs social-circle" style="left:606px"><svg viewBox="0 0 24 24"><path d="M12 3l10 9h-3v9h-5v-6h-4v6H5v-9H2z"/></svg></div>
<div class="abs social-label" style="left:91px">LIKE US</div>
<div class="abs social-label" style="left:192px">FOLLOW US</div>
<div class="abs social-label" style="left:287px">CORVANE LIFE</div>
<div class="abs social-label" style="left:383px">CONNECT WITH US</div>
<div class="abs social-label" style="left:479px">OUR BLOG</div>
<div class="abs social-label" style="left:571px">CORPORATE SITE</div>

<div class="abs kitten-photo" role="img" aria-label="Photo of a tabby kitten crouching"></div>
<h2 class="abs welcome-title">WELCOME!</h2>
<div class="abs welcome-text">
  <p>Praesent vestibulum molestie lacus. Aeneanum nonummy hendrerit mauris. Phasellus portame. Fusce suscipit varius mium sociis natoquemetun penatibus et magnis dis parturient.</p>
  <p>Montes, nascetur ridiculus mus. Nulla dui. Fusce feugiat&nbsp; malesuada odio morbi nunc odio gravida atem cursus nluctus lorem maecenas tristique orci ac sem. Duis ultricies pharetra.</p>
</div>

<h2 class="abs news-heading">LATEST NEWS</h2>
<div class="abs news-date" style="top:586px"><b>25</b><span>JUL</span></div>
<div class="abs news-title" style="top:586px">FUSCE SUSCIPIT VARIUS MIUM SOCIIS NATOQUEMETUN</div>
<p class="abs news-text" style="top:632px">Montes, nascetur ridiculus mus. Nulla dui. Fusce feugiat&nbsp; malesuada odio morbi nunc. <a>READ MORE</a></p>
<div class="abs news-date" style="top:682px"><b>25</b><span>JUL</span></div>
<div class="abs news-title" style="top:682px">FUSCE SUSCIPIT VARIUS MIUM SOCIIS NATOQUEMETUN</div>
<p class="abs news-text" style="top:728px">Montes, nascetur ridiculus mus. Nulla dui. Fusce feugiat&nbsp; malesuada odio morbi nunc. <a>READ MORE</a></p>

<div class="abs rule" style="top:822px"></div>

<div class="abs client-frame" style="left:38px"><div class="client-photo" role="img" aria-label="Photo of a woman holding a kitten" style="background:linear-gradient(135deg,#7d8a6a,#c9bfb0)"></div></div>
<div class="abs client-frame" style="left:229px"><div class="client-photo" role="img" aria-label="Photo of a smiling woman lying beside a dog" style="background:linear-gradient(135deg,#b7894f,#e4c9a0)"></div></div>
<div class="abs client-frame" style="left:425px"><div class="client-photo" role="img" aria-label="Photo of a woman with a small white dog" style="background:linear-gradient(135deg,#b9bf6a,#e9e4c0)"></div></div>
<div class="abs client-frame" style="left:615px"><div class="client-photo" role="img" aria-label="Photo of a woman holding a small brown dog" style="background:linear-gradient(135deg,#f08aa0,#58cfc8)"></div></div>

<div class="abs client-name" style="left:38px">Nora Pell</div>
<div class="abs client-name" style="left:228px">Delia Fenwick</div>
<div class="abs client-name" style="left:422px">Tessa Marlow</div>
<div class="abs client-name" style="left:612px">Joan Aldridge</div>
<p class="abs client-text" style="left:35px">Montes, nascetur ridiculus mus. Nulla dui.Fusce feugiat&nbsp; malesuada odio morbi nunc odio gravida atem cursus nluctus lorem maecenas.</p>
<p class="abs client-text" style="left:225px">Montes, nascetur ridiculus mus. Nulla dui.Fusce feugiat&nbsp; malesuada odio morbi nunc odio gravida atem cursus nluctus lorem maecenas.</p>
<p class="abs client-text" style="left:419px">Montes, nascetur ridiculus mus. Nulla dui.Fusce feugiat&nbsp; malesuada odio morbi nunc odio gravida atem cursus nluctus lorem maecenas.</p>
<p class="abs client-text" style="left:610px">Montes, nascetur ridiculus mus. Nulla dui.Fusce feugiat&nbsp; malesuada odio morbi nunc odio gravida atem nluctus lorem maecenas.</p>

<div class="abs rule" style="top:1069px"></div>
<a class="abs more-link">more testimonials <i></i></a>

<footer class="abs footer"><strong>THE CORVANE AGENCY</strong><span>© 2013. All Rights Reserved</span></footer>

</body>
</html>
```